Business Card Design Project

We would like a business card designed for our Tulip & Acorn Club. Although we do want to be creative, it is important for us to maintain branding, therefore most of the design will be copied from our website.
We do want people to know what it is all about, so we included some of the wording. However we rely heavily on your advice and if you think it is better without then as long as design is good we are willing to consider it.
All designs submitted must follow print-ready design rules. Use only CMYK colours
Target Market(s)
Mothers and mothers-to-be
Industry/Entity Type
Business
Look and feel
Each slider illustrates characteristics of the customer's brand and the style your logo design should communicate.

```html
<!DOCTYPE html>
<html lang="en">
<head>
<meta charset="utf-8">
<title>Tulip &amp; Acorn Club – Business Card</title>
<link href="https://fonts.googleapis.com/css2?family=Crimson+Text:wght@400;700&display=swap" rel="stylesheet">
<style>
  :root {
    --backdrop: #3b3936;
    --card-yellow: #f7c53a;
    --band-light: #f2aa2c;
    --band-dark: #e3951b;
    --band-edge: #c27812;
    --plaque: #f6c83f;
    --plaque-edge: #d9a024;
    --stitch: #b08a3a;
    --ink: #3e3422;
  }
  html, body {
    margin: 0;
    width: 1200px;
    height: 1000px;
    overflow: hidden;
    background: var(--backdrop);
  }
  .canvas {
    position: relative;
    width: 1200px;
    height: 1000px;
  }
  .business-card {
    position: absolute;
    left: 250px;
    top: 300px;
    width: 700px;
    height: 400px;
    border-radius: 24px;
    overflow: hidden;
    background: var(--card-yellow);
    box-shadow: 0 10px 30px rgba(0,0,0,0.45);
    font-family: "Crimson Text", Georgia, serif;
    color: var(--ink);
  }
  .card-art {
    position: absolute;
    inset: 0;
    width: 700px;
    height: 400px;
  }
  .club-name {
    position: absolute;
    left: 40px;
    top: 45px;
    width: 620px;
    height: 70px;
    line-height: 70px;
    text-align: center;
    font-size: 40px;
    font-weight: 400;
    margin: 0;
  }
  .contact-block {
    position: absolute;
    left: 0;
    top: 180px;
    width: 700px;
    text-align: center;
  }
  .person-name {
    font-size: 40px;
    line-height: 48px;
    margin: 0 0 14px;
    font-weight: 400;
  }
  .contact-line {
    font-size: 20px;
    line-height: 25px;
    margin: 0;
  }
  .contact-line .label { font-weight: 700; }
  .contact-line .gap { display: inline-block; width: 18px; }
  .website {
    font-size: 25px;
    margin: 26px 0 0;
    letter-spacing: 0.3px;
  }
</style>
</head>
<body>
<main class="canvas">
  <article class="business-card">
    <svg class="card-art" viewBox="0 0 700 400" aria-hidden="true">
      <defs>
        <pattern id="band-stripes" width="44" height="400" patternUnits="userSpaceOnUse">
          <rect width="22" height="400" fill="var(--band-light)"/>
          <rect x="22" width="22" height="400" fill="var(--band-dark)"/>
        </pattern>
        <linearGradient id="band-shade" x1="0" x2="1" y1="0" y2="0">
          <stop offset="0" stop-color="#8a4e05" stop-opacity="0.35"/>
          <stop offset="0.5" stop-color="#8a4e05" stop-opacity="0"/>
          <stop offset="1" stop-color="#8a4e05" stop-opacity="0.35"/>
        </linearGradient>
      </defs>
      <path class="header-band" d="M0,0 H700 V178 Q350,100 0,186 Z" fill="url(#band-stripes)"/>
      <path d="M0,0 H700 V178 Q350,100 0,186 Z" fill="url(#band-shade)"/>
      <path class="band-edge" d="M0,186 Q350,100 700,178" fill="none" stroke="var(--band-edge)" stroke-width="3" opacity="0.7"/>
      <path class="plaque" d="M52,45 H648 A12 12 0 0 0 660 57 V103 A12 12 0 0 0 648 115 H52 A12 12 0 0 0 40 103 V57 A12 12 0 0 0 52 45 Z" fill="var(--plaque)" stroke="var(--plaque-edge)" stroke-width="2"/>
      <path class="plaque-stitch" d="M58,52 H642 A10 10 0 0 0 652 62 V98 A10 10 0 0 0 642 108 H58 A10 10 0 0 0 48 98 V62 A10 10 0 0 0 58 52 Z" fill="none" stroke="var(--stitch)" stroke-width="1.2" stroke-dasharray="4 3"/>
    </svg>

    <h1 class="club-name">Tulip &amp; Acorn Club</h1>

    <div class="contact-block">
      <p class="person-name">Clara Hollins</p>
      <p class="contact-line"><span class="label">Tel:</span> 021 555 0198<span class="gap"></span><span class="label">Mobile:</span> 021 555 0198</p>
      <p class="contact-line"><span class="label">Email:</span> hello@tulipacornclub.com</p>
      <p class="website">www.tulipacornclub.com</p>
    </div>
  </article>
</main>
</body>
</html>
```